Web Design Project - Quillmore Analytics

I am a Mechanical Engineer running a one person consulting firm at this point. The hope is to expand in the future, but for now I simply need a website that conveys a professional appearance, and allows potential and existing clients to find me. Website design displaying contact information, CV for download, capabilities, past projects, etc. I've included four examples below from companies that provided the same service. I've only provided these as general reference for the type of work I do and how others have chosen to display this information. The design is completely at your discretion.

I've included the current Logo in the uploaded files section. I will provide content as requried.

http://www.torvanmech.com/
http://www.halberic.com/
http://www.rumblaxsystems.com/
http://dorwickmotive.net/

Industry/Entity Type

Consulting

```html
<!DOCTYPE html>
<html lang="en">
<head>
<meta charset="utf-8">
<title>Quillmore Analytics — Engineering Consulting</title>
<link href="https://fonts.googleapis.com/css2?family=Arimo:wght@400;700&family=Open+Sans:wght@400;600&display=swap" rel="stylesheet">
<style>
  :root {
    --orange: #de8035;
    --orange-text: #e07f33;
    --ink: #3d3d3d;
    --body: #4a4a4a;
    --band: #e6e7e6;
    --rule: #d9d9d9;
    --white: #ffffff;
  }
  * { margin: 0; padding: 0; box-sizing: border-box; }
  html, body { width: 1152px; height: 1200px; overflow: hidden; background: var(--white); }
  body { position: relative; font-family: "Arimo", Arial, sans-serif; color: var(--body); }
  .abs { position: absolute; }
  .heading { font-family: "Open Sans", Arial, sans-serif; }

  .brand { left: 106px; top: 50px; display: flex; align-items: center; gap: 8px; }
  .brand-mark { width: 14px; height: 14px; background: var(--orange); }
  .brand-name { font-family: "Open Sans", Arial, sans-serif; font-weight: 600; font-size: 20px; color: var(--orange); letter-spacing: 0.5px; }

  .call-now { right: 100px; top: 58px; font-family: "Open Sans", Arial, sans-serif; font-size: 19px; color: var(--orange-text); }

  .main-nav { left: 92px; top: 107px; width: 960px; height: 47px; background: var(--orange); display: flex; align-items: center; padding-left: 20px; gap: 28px; }
  .main-nav a { color: var(--white); text-decoration: none; font-size: 13px; }

  .hero-title { left: 128px; top: 238px; font-size: 19px; line-height: 26px; color: var(--ink); text-transform: uppercase; }
  .hero-title .accent { color: var(--orange-text); }
  .hero-text { left: 130px; top: 300px; width: 345px; font-size: 12px; line-height: 16.5px; }
  .btn-cv { left: 159px; top: 417px; width: 207px; height: 39px; background: linear-gradient(#ececec, #d9d9d9); display: flex; align-items: center; justify-content: center; font-family: "Open Sans", Arial, sans-serif; font-size: 15px; color: var(--ink); text-decoration: none; }

  .hero-photo { left: 614px; top: 168px; width: 420px; height: 342px; background: linear-gradient(160deg, #e9e3df 0%, #8a7a70 45%, #4a4d55 100%); }
  .slider-dots { left: 922px; top: 481px; display: flex; gap: 9px; }
  .slider-dots span { width: 11px; height: 11px; border-radius: 50%; background: var(--white); }

  .welcome-band { left: 0; top: 510px; width: 1152px; height: 175px; background: var(--band); }
  .section-title { font-family: "Open Sans", Arial, sans-serif; font-size: 14px; color: var(--orange-text); text-transform: uppercase; }
  .copy { font-size: 12px; line-height: 16.3px; }
  .read-more { font-weight: 700; color: var(--ink); display: block; }
  .welcome-photo { left: 862px; top: 558px; width: 123px; height: 111px; background: linear-gradient(135deg, #dfe7ec, #c9a58c 55%, #8fb0c8); }

  .project-thumb { top: 801px; height: 128px; }

  .cap-list { left: 805px; top: 747px; width: 247px; list-style: none; }
  .cap-list li { font-size: 11.5px; font-weight: 700; color: var(--ink); height: 27px; line-height: 20px; border-bottom: 1px solid var(--rule); }
  .cap-list li:last-child { border-bottom: none; }

  .contact-info { left: 805px; top: 962px; font-size: 12px; line-height: 16.3px; color: var(--ink); }

  .footer-rule { left: 0; top: 1119px; width: 1152px; height: 2px; background: var(--rule); }
  .footer-nav { left: 130px; top: 1132px; display: flex; gap: 28px; }
  .footer-nav a { color: var(--orange-text); text-decoration: none; font-size: 13px; }
  .copyright { left: 130px; top: 1155px; font-size: 10.5px; font-weight: 700; color: #8a8a8a; }
  .social { left: 923px; top: 1135px; display: flex; gap: 7px; }
  .social span { width: 29px; height: 29px; border-radius: 4px; }
</style>
</head>
<body>
  <div class="abs brand"><span class="brand-mark"></span><span class="brand-name">Quillmore Analytics</span></div>
  <div class="abs call-now">CALL NOW: 123 (555)-5678</div>

  <nav class="abs main-nav">
    <a href="#">HOME</a><a href="#">ABOUT ME</a><a href="#">MY CV</a><a href="#">PROJECTS</a><a href="#">CAPABILITIES</a><a href="#">CONTACT</a>
  </nav>

  <h1 class="abs hero-title heading" style="font-weight:400"><span class="accent">Lorem ipsum dolor</span> sit amet<br>consectetur adipisicing elit</h1>
  <p class="abs hero-text">Tempor incididunt ut labore et dolore magna aliqua. Ut enim ad minim veniam, quis nostrud exercitation ullamco laboris nisi ut aliquip ex ea commodo consequat.</p>
  <a class="abs btn-cv" href="#">DOWNLOAD MY CV</a>

  <div class="abs hero-photo" role="img" aria-label="Portrait of the engineer in a dark suit and striped tie"></div>
  <div class="abs slider-dots"><span></span><span></span><span></span><span></span></div>

  <section class="abs welcome-band"></section>
  <h2 class="abs section-title" style="left:125px;top:528px;font-weight:400">Welcome to my site</h2>
  <p class="abs copy" style="left:125px;top:553px;width:690px">Sed ut perspiciatis unde omnis iste natus error sit voluptatem accusantium doloremque laudantium, totam rem aperiam, eaq ipsa quae ab illo inventore veritatis et quasi architecto beatae vitae dicta sunt explicabo. Nemo enim ipsam voluptatem quia voluptas sit aspernatur aut odit aut fugit, sed quia consequuntur magni dolores eos qui ratione voluptatem sequi nesciunt. S ut perspiciatis unde omnis iste natus error sit voluptatem accusantium doloremque laudantium, totam rem aperiam, eaque quae ab illo inventore veritatis et quasi architecto beatae vitae dicta sunt explicabo.<span class="read-more">Read more..</span></p>
  <div class="abs welcome-photo" role="img" aria-label="Smiling engineer with colleagues in the background"></div>

  <h2 class="abs section-title" style="left:127px;top:701px;font-weight:400">My Projects</h2>
  <p class="abs copy" style="left:126px;top:741px;width:632px">Sed ut perspiciatis unde omnis iste natus error sit voluptatem accusantium doloremque laudantium ipsa quae ab illo inventore veritatis et quasi architecto beatae vitae dicta sunt explicabo</p>
  <div class="abs project-thumb" style="left:126px;width:203px;background:linear-gradient(135deg,#e6f1f8,#9cc3dc 60%,#cfe2ee)" role="img" aria-label="Interlocking metal gears"></div>
  <div class="abs project-thumb" style="left:336px;width:206px;background:linear-gradient(120deg,#4a3d33,#8a7565 55%,#e8e3de)" role="img" aria-label="Hand holding a stylus over a handheld device"></div>
  <div class="abs project-thumb" style="left:548px;width:207px;background:linear-gradient(160deg,#3a3a3a 0%,#a0163f 35%,#c11d4c 100%)" role="img" aria-label="Automotive services promotional banner"></div>
  <p class="abs copy" style="left:125px;top:967px;width:632px">Sed ut perspiciatis unde omnis iste natus error sit voluptatem accusantium doloremque laudantium, totam rem aperiam, eaq ipsa quae ab illo inventore veritatis et quasi architecto beatae vitae dicta sunt explicabo. Nemo enim ipsam voluptatem quia voluptas sit aspernatur aut odit aut fugit, sed quia consequuntur magni dolores eos qui ratione voluptatem sequi nesciunt.<span class="read-more">Read more..</span></p>

  <h2 class="abs section-title" style="left:791px;top:701px;font-weight:400">Capabilities</h2>
  <ul class="abs cap-list">
    <li>Sed ut perspiciatis unde omnis iste</li>
    <li>Natus error sit voluptatem</li>
    <li>Accusantium doloremque laudantium</li>
    <li>Lpsa quae ab</li>
    <li>Nventore veritatis et quasi architecto</li>
    <li>Beatae vitae dicta sunt explicabo</li>
  </ul>

  <h2 class="abs section-title" style="left:791px;top:933px;font-weight:400">Contact Info</h2>
  <address class="abs contact-info" style="font-style:normal">Sed ut perspiciatis unde<br>error sit voluptatem<br>doloremque<br>NY - 123456<br><br>Ph: 123 (555 ) - 567<br>Email: info@yourcompany.com</address>

  <div class="abs footer-rule"></div>
  <nav class="abs footer-nav">
    <a href="#">HOME</a><a href="#">ABOUT ME</a><a href="#">MY CV</a><a href="#">PROJECTS</a><a href="#">CAPABILITIES</a><a href="#">CONTACT</a>
  </nav>
  <div class="abs copyright">COPYRIGHT 2013. ALL RIGHTS RESERVED.</div>
  <div class="abs social">
    <span style="background:#4fc3ee" role="img" aria-label="Social link"></span>
    <span style="background:#c4261d" role="img" aria-label="Video channel link"></span>
    <span style="background:#3b5a9a" role="img" aria-label="Social profile link"></span>
  </div>
</body>
</html>
```